CALDER VALE

Labels for Men's Skin Care. Organic, target 25-35 The label will be 2x3.5 on a 4oz amber bottle. 3 labels with the information shown on the uploaded sample.
Our product is a e-commerce built to help my 24 year old twin sons have a business of their own. Although it will be sold online they will also do foot work and sell to barbers at barber shops using as a mist on customers after shaving. So we want something that will attract male customers and will look good in a modern Barbershop. This is there shot and packaging is very very important. So if you could help us out with a great label we would be working with you in the future for package design. Our line will have several mens Organic natural skin care cleanser, mask toners and moisturizers..Thank you for your help. We also hope to put our products in beauty supply shops. So it needs to stand out as a mans product but still be traditional male product. Oh be creative mind that you are and remember we are trying to build a brand that attracts 25-35 male. Thank you

Hello, I just wanted to let you know that I am up working very late.

for anyone on the other side of the world up and working. I sleep about
3 hours.. So I'll be up for a few more hours and then up again around 5am my time

Good morning... I just wanted to say I will need three labels.. The words on all three are not that different and will fit pretty much the same on all three. So if you could work with one showing how the colors might be a little different on the other two you can do that with just the one label Just to make it easier on you if you like.. we can fix the other two once I find the right label,  Thank you it is 3am here.. still working.. I love it.

Target Market(s)

MALE 25-35

Industry/Entity Type

E-Commerce

Requirements
Must have
• final design must be fitted to the dieline uploaded.

```html
<!DOCTYPE html>
<html lang="en">
<head>
<meta charset="utf-8">
<title>Calder Vale – Manhood Freshener Label</title>
<link rel="stylesheet" href="https://fonts.googleapis.com/css2?family=Arimo:wght@400&family=Dancing+Script:wght@400&display=swap">
<style>
  :root {
    --label-deep: #1b1142;
    --label-violet: #2e1d6e;
    --label-mid: #3a2a8a;
    --streak-blue: rgba(79,143,214,0.55);
    --streak-light: rgba(159,208,245,0.5);
    --title-white: #ffffff;
    --script-grey: #d9d9de;
    --accent-green: #8cc63f;
    --page-bg: #ffffff;
  }
  html, body {
    margin: 0;
    padding: 0;
    width: 686px;
    height: 1200px;
    overflow: hidden;
    background: var(--page-bg);
  }
  .label {
    position: relative;
    width: 686px;
    height: 1200px;
    border-radius: 42px;
    overflow: hidden;
    background: var(--label-deep);
    font-family: "Arimo", Arial, sans-serif;
    color: var(--title-white);
  }
  .light-streaks {
    position: absolute;
    inset: 0;
    background:
      radial-gradient(ellipse 70% 45% at 95% 5%, var(--label-deep) 0%, transparent 100%),
      radial-gradient(ellipse 60% 40% at 95% 95%, var(--label-deep) 0%, transparent 100%),
      linear-gradient(132deg,
        transparent 6%,
        var(--streak-blue) 16%,
        var(--streak-light) 22%,
        transparent 32%,
        var(--streak-blue) 42%,
        var(--streak-light) 49%,
        var(--streak-blue) 56%,
        transparent 68%),
      linear-gradient(160deg, var(--label-violet) 0%, var(--label-mid) 45%, var(--label-violet) 80%, var(--label-deep) 100%);
  }
  .brand-name {
    position: absolute;
    right: 38px;
    top: 59px;
    margin: 0;
    text-align: right;
    font-weight: 400;
    font-size: 140px;
    line-height: 135px;
  }
  .brand-name span { display: block; }
  .product-type {
    position: absolute;
    left: 104px;
    top: 343px;
    margin: 0;
    font-family: "Dancing Script", cursive;
    font-weight: 400;
    font-size: 70px;
    line-height: 70px;
    color: var(--script-grey);
    letter-spacing: 3px;
  }
  .claim-band {
    position: absolute;
    left: 0;
    top: 0;
    width: 686px;
    height: 1200px;
  }
  .claim-band text {
    font-family: "Arimo", Arial, sans-serif;
    font-size: 48px;
    fill: var(--accent-green);
  }
  .benefit {
    position: absolute;
    left: 0;
    width: 662px;
    top: 885px;
    margin: 0;
    text-align: center;
    font-size: 48px;
    line-height: 53px;
  }
  .volume {
    position: absolute;
    left: 0;
    width: 688px;
    top: 1121px;
    margin: 0;
    text-align: center;
    font-size: 48px;
    line-height: 54px;
  }
</style>
</head>
<body>
  <div class="label">
    <div class="light-streaks" role="img" aria-label="Flowing blue light streaks sweeping diagonally across a deep violet background"></div>

    <h1 class="brand-name"><span>Calder</span><span>Vale</span></h1>
    <p class="product-type">Manhood Freshener</p>

    <svg class="claim-band" viewBox="0 0 686 1200">
      <text x="98" y="478" textLength="668" lengthAdjust="spacingAndGlyphs" transform="rotate(41 98 478)">ORGANIC NATURAL HEALING</text>
    </svg>

    <p class="benefit">Maintain Groin<br>Freshness &amp; Dryness<br>While Reducing Skin<br>Irritation and Chafing</p>
    <p class="volume">3.5 fl oz 103 ml</p>
  </div>
</body>
</html>
```